CBD online business for pets and pet parents needs a new website

We need a website for my new online business. I have left a job of 25 years to do my passion. Helping Pets Live healthy and happy lives. I would like to provide my story so that our customer will know why I have started this business-To help!We will be providing all natural CBD (Hemp) products, specialty items, memorials as well as some products for pet parents. We would like our landing page to have our mission, be informative and easy to navigate and maybe feature our treats and oils for pets. We will need a page for pet products, a page for pet memorials, a page for pet lover products and a page for pet parent products.

Target Market(s)

millennials, boomers, pet lovers

Coding

Coded - Design and coding required

Number of Pages Required

5+ page

Colors
33b8a4

Requirements
Nice to have
• diagram of hemp oil extract benefits for dogs and people

```html
<!DOCTYPE html>
<html lang="en">
<head>
<meta charset="utf-8">
<title>Tailwise – Pet Products</title>
<link href="https://fonts.googleapis.com/css2?family=Montserrat:wght@400;500;600;700;800&family=Kaushan+Script&display=swap" rel="stylesheet">
<style>
:root{
  --teal:#12a6a8;
  --ink:#2b2b2b;
  --line:#e2e2e2;
  --frame:#e0e0e0;
  --mist:#e6f5f5;
  --star:#f5a623;
  --footer:#2c2d2f;
  --white:#ffffff;
}
*{margin:0;padding:0;box-sizing:border-box}
html,body{width:1200px;height:2325px;overflow:hidden}
body{position:relative;background:var(--white);font-family:"Montserrat",sans-serif;color:var(--ink)}
.abs{position:absolute}
.script{font-family:"Kaushan Script",cursive;font-weight:400;color:var(--teal)}

/* header */
.top-rule{left:0;top:0;width:1200px;height:3px;background:var(--teal)}
.lang{left:127px;top:21px;width:115px;height:34px;border:1px solid #444;border-radius:17px;font-size:12.5px;display:flex;align-items:center;padding-left:18px;gap:7px}
.lang .dot{width:13px;height:13px;border-radius:50%;background:#c8283a;box-shadow:inset -5px -5px 0 #1d3b8a}
.social-top{left:265px;top:29px;display:flex;gap:15px}
.social-top span{width:18px;height:18px;border-radius:50%;background:#9c9c9c;display:block}
.social-top span:nth-child(2){background:#2b2b2b;border-radius:2px}
.rule{height:1px;background:#cfcfcf;top:72px}
.nav a{position:absolute;top:92px;font-size:14.5px;color:var(--ink);text-decoration:none}
.nav a.active,.nav a.hl{color:var(--teal)}
.nav-under{left:358px;top:121px;width:109px;height:3px;background:var(--teal)}
.search{left:791px;top:21px;width:185px;height:34px;border:1px solid #444;border-radius:17px;font-size:11.5px;color:#666;display:flex;align-items:center;padding-left:20px}
.search .btn{position:absolute;right:2px;top:2px;width:36px;height:28px;border-radius:0 14px 14px 0;background:var(--teal)}
.cart{left:998px;top:29px;font-size:13px;display:flex;gap:8px;align-items:center}
.header-base{left:0;top:0;width:1200px;height:126px;background:var(--white)}
.brand-tab{left:492px;top:60px;width:216px;height:93px;background:var(--white);border-radius:0 0 60px 60px;z-index:3}
.brand{left:490px;top:18px;width:220px;z-index:4;text-align:center}
.brand .mark{width:60px;height:60px;border-radius:50%;background:var(--teal);margin:0 auto 16px}
.brand .name{font-size:25px;font-weight:700;color:var(--teal);letter-spacing:-.5px}

/* hero */
.hero{left:0;top:126px;width:1200px;height:324px}
.hero-title{left:161px;top:174px;font-size:50px;font-weight:700;color:var(--teal);letter-spacing:-1.5px;line-height:60px}
.hero-sub{left:161px;top:236px;font-size:34px;line-height:44px}
.crumbs{left:161px;top:424px;font-size:12.5px;color:#444;display:flex;gap:18px}
.crumbs .cur{color:var(--teal);font-weight:500}

/* heading */
.sec-mark{left:580px;top:510px;width:40px;height:44px;border-radius:50%;background:radial-gradient(circle at 50% 60%,#3a3a3a 0 42%,var(--teal) 43% 100%)}
.sec-title{left:0;width:1200px;top:566px;text-align:center;font-size:35px;font-weight:700;letter-spacing:-1px}
.sec-title .script{font-size:38px;letter-spacing:0}
.sec-rule{left:576px;top:618px;width:48px;height:3px;background:var(--teal)}

/* sidebar */
.cats{left:161px;top:645px;width:210px;border:1px solid var(--line)}
.cats h3{background:var(--teal);color:#fff;font-size:15.5px;font-weight:700;letter-spacing:-.5px;height:41px;line-height:41px;padding-left:17px}
.cats li{list-style:none;height:38px;border-top:1px solid var(--line);display:flex;align-items:center;gap:13px;padding-left:20px;font-size:13px}
.cats li i{width:15px;height:15px;border-radius:50%;background:var(--teal);display:block}

/* toolbar */
.toolbar{left:393px;top:644px;width:647px;height:42px;border:1px solid var(--line);font-size:12px;color:#444}
.toolbar .grid{position:absolute;left:16px;top:13px;width:15px;height:15px;background:
 linear-gradient(var(--teal),var(--teal)) 0 0/6px 6px no-repeat,
 linear-gradient(var(--teal),var(--teal)) 9px 0/6px 6px no-repeat,
 linear-gradient(var(--teal),var(--teal)) 0 9px/6px 6px no-repeat,
 linear-gradient(var(--teal),var(--teal)) 9px 9px/6px 6px no-repeat}
.toolbar .list{position:absolute;left:46px;top:14px;width:15px;height:13px;background:repeating-linear-gradient(#bbb 0 1px,transparent 1px 5px)}
.toolbar .sep{position:absolute;left:83px;top:11px;width:1px;height:20px;background:#ccc}
.toolbar .count{position:absolute;left:106px;top:13px}
.toolbar .sortl{position:absolute;left:434px;top:13px}
.toolbar .sort{position:absolute;left:487px;top:6px;width:150px;height:28px;border:1px solid #ccc;padding:6px 9px;font-size:12.5px;color:var(--ink)}
.toolbar .sort::after{content:"";position:absolute;right:12px;top:9px;width:5px;height:5px;border-right:1.5px solid #333;border-bottom:1.5px solid #333;transform:rotate(45deg)}

/* products */
.card{width:203px;text-align:center}
.card .frame{height:243px;border:7px solid var(--frame);position:relative;background:#fff;overflow:hidden}
.card .shot{position:absolute;inset:0}
.card .price{margin-top:20px;font-size:20px;font-weight:500;color:var(--teal)}
.card .title{margin-top:9px;font-size:14.5px;font-weight:600;letter-spacing:-.6px}
.card .rate{margin-top:10px;font-size:12.5px;color:#555}
.card .rate b{color:var(--star);font-weight:400;letter-spacing:4px;font-size:13px}
.add{position:absolute;left:0;right:0;bottom:0;height:38px;background:var(--teal);color:#fff;font-size:15px;font-weight:600;line-height:38px}
.tone-leather{background:radial-gradient(ellipse 60% 42% at 50% 50%,#9a6a48 0%,#c9a88f 45%,#f3ece6 75%,#fff 100%)}
.tone-oil{background:radial-gradient(ellipse 48% 50% at 52% 46%,#1f3336 0%,#3f8a8c 40%,#d9ecec 75%,#fff 100%)}
.tone-jar{background:radial-gradient(ellipse 50% 48% at 50% 48%,#2f3a3d 0%,#6e8b8d 45%,#e7eeee 76%,#fff 100%)}
.tone-bottle{background:radial-gradient(ellipse 28% 50% at 50% 50%,#1b1e20 0%,#4d5a5c 50%,#e9eded 85%,#fff 100%)}
.tone-black{background:radial-gradient(ellipse 60% 40% at 50% 50%,#2a2a2a 0%,#777 45%,#eeeeee 75%,#fff 100%)}
.tone-wood{background:radial-gradient(ellipse 65% 35% at 50% 50%,#c8b277 0%,#dccf9f 50%,#f5f0e0 78%,#fff 100%)}
.tone-hoodie{background:radial-gradient(ellipse 52% 50% at 50% 50%,#1c1c1c 0%,#4a4a4a 50%,#e6e6e6 82%,#fff 100%)}
.tone-slate{background:radial-gradient(ellipse 60% 38% at 50% 50%,#3a4150 0%,#9aa1a8 45%,#eef0f2 76%,#fff 100%)}

.divider{left:393px;top:1793px;width:647px;height:1px;background:var(--line)}
.pager{left:626px;top:1816px;display:flex;gap:8px}
.pager span{width:30px;height:30px;border-radius:50%;border:1px solid #ccc;font-size:14px;display:flex;align-items:center;justify-content:center;color:#444}
.pager span.on{background:var(--teal);border-color:var(--teal);color:#fff}

/* footer */
.footer{left:0;top:1900px;width:1200px;height:368px}
.f-head{font-size:15px;font-weight:700;color:#fff;letter-spacing:-.6px}
.f-head .script{font-size:16px;letter-spacing:0}
.f-rule{width:27px;height:2px;background:var(--teal);margin-top:12px}
.f-links{list-style:none;color:#e6e6e6;font-size:13px;margin-top:13px}
.f-links li{height:24.5px}
.f-text{color:#e6e6e6;font-size:12.5px}
.ico{position:absolute;left:0;width:14px;height:16px}
.field{width:210px;height:37px;border:1px solid #777;border-radius:19px;color:#aaa;font-size:11.5px;padding:11px 15px;letter-spacing:.8px}
.signup{width:113px;height:44px;border-radius:22px;background:var(--teal);color:#fff;font-size:15px;font-weight:600;text-align:center;line-height:44px}
.f-social span{display:inline-block;width:30px;height:30px;border-radius:50%;border:1px solid #777;margin-right:4px}
.f-social span.on{background:var(--teal);border-color:var(--teal)}
.bottom{left:0;top:2268px;width:1200px;height:57px;background:var(--teal);color:#fff;font-size:12.5px;letter-spacing:1px}
</style>
</head>
<body>

<!-- header -->
<div class="abs header-base"></div>
<div class="abs top-rule"></div>
<div class="abs lang"><span class="dot"></span>English ▾</div>
<div class="abs social-top" aria-label="Social links"><span></span><span></span><span></span><span></span><span></span></div>
<div class="abs rule" style="left:127px;width:343px"></div>
<div class="abs rule" style="left:730px;width:343px"></div>
<nav class="nav">
  <a style="left:129px">Home</a>
  <a style="left:240px">About Us</a>
  <a class="active" style="left:361px">Pet Products ▾</a>
  <a style="left:731px">Our Mission</a>
  <a class="hl" style="left:846px">Benefits</a>
  <a style="left:933px">Blog</a>
  <a style="left:995px">Contact Us</a>
</nav>
<div class="abs nav-under"></div>
<div class="abs search">Search...<span class="btn">
  <svg width="36" height="28" viewBox="0 0 36 28"><circle cx="17" cy="13" r="5" fill="none" stroke="#fff" stroke-width="2"/><line x1="21" y1="17" x2="24" y2="20" stroke="#fff" stroke-width="2"/></svg></span></div>
<div class="abs cart">
  <svg width="17" height="15" viewBox="0 0 17 15"><path d="M0 1h3l2 9h9l2-7H5" fill="none" stroke="#222" stroke-width="2"/><circle cx="6" cy="13" r="1.5" fill="#222"/><circle cx="13" cy="13" r="1.5" fill="#222"/></svg>
  Cart (0)</div>

<!-- hero -->
<svg class="abs hero" viewBox="0 0 1200 324" role="img" aria-label="Photo of a smiling woman hugging a happy dog outdoors">
  <defs>
    <linearGradient id="sky" x1="0" x2="1" y1="0" y2="0">
      <stop offset="0" stop-color="#d9ddd2"/><stop offset=".4" stop-color="#e7e2d6"/><stop offset=".62" stop-color="#cdb48f"/><stop offset=".8" stop-color="#9b7554"/><stop offset="1" stop-color="#5f4331"/>
    </linearGradient>
    <radialGradient id="warm" cx=".74" cy=".5" r=".28">
      <stop offset="0" stop-color="#e6c79a" stop-opacity=".9"/><stop offset=".6" stop-color="#caa274" stop-opacity=".5"/><stop offset="1" stop-color="#caa274" stop-opacity="0"/>
    </radialGradient>
    <radialGradient id="haze" cx=".2" cy=".25" r=".35">
      <stop offset="0" stop-color="#f2efe6" stop-opacity=".9"/><stop offset="1" stop-color="#f2efe6" stop-opacity="0"/>
    </radialGradient>
  </defs>
  <rect width="1200" height="324" fill="url(#sky)"/>
  <rect width="1200" height="324" fill="url(#warm)"/>
  <rect width="1200" height="324" fill="url(#haze)"/>
  <path d="M0 112 Q560 420 1200 110 L1200 324 L0 324Z" fill="#d6eeee" opacity=".9"/>
  <path d="M0 172 Q560 400 1200 114 L1200 140 Q560 470 0 190Z" fill="var(--teal)"/>
  <path d="M0 190 Q560 470 1200 140 L1200 324 L0 324Z" fill="var(--mist)"/>
</svg>
<div class="abs brand-tab"></div>
<div class="abs brand"><div class="mark"></div><div class="name">Tailwise</div></div>
<h1 class="abs hero-title">Helping Pets</h1>
<p class="abs hero-sub script" style="color:var(--ink)">Live healthy and happy lives</p>
<div class="abs crumbs"><span>Home</span><span>›</span><span class="cur">Pet Products</span></div>

<!-- section heading -->
<div class="abs sec-mark"></div>
<h2 class="abs sec-title">Pet <span class="script">Products</span></h2>
<div class="abs sec-rule"></div>

<!-- categories -->
<aside class="abs cats">
  <h3>Categories</h3>
  <ul>
    <li><i></i>Treats And Oils</li>
    <li><i></i>Pet Products</li>
    <li><i></i>Pet Lover Products</li>
    <li><i></i>Pet Memorials</li>
    <li><i></i>Pet Parent Products</li>
  </ul>
</aside>

<!-- toolbar -->
<div class="abs toolbar">
  <span class="grid"></span><span class="list"></span><span class="sep"></span>
  <span class="count">Showing all 9 Products</span>
  <span class="sortl">Sort By :</span>
  <span class="sort">Default</span>
</div>

<!-- products -->
<div class="abs card" style="left:393px;top:703px"><div class="frame"><div class="shot tone-leather" role="img" aria-label="Brown leather dog collar"></div></div><div class="price">$ 385.00</div><div class="title">Brown Roamer Collar</div><div class="rate"><b>★★★★★</b> (77)</div></div>
<div class="abs card" style="left:615px;top:703px"><div class="frame"><div class="shot tone-oil" role="img" aria-label="Hemp oil dropper bottle with box"></div><div class="add">🛒 Add To Cart</div></div><div class="price">$ 385.00</div><div class="title">TW Extra Strength</div><div class="rate"><b>★★★★★</b> (77)</div></div>
<div class="abs card" style="left:836px;top:703px"><div class="frame"><div class="shot tone-jar" role="img" aria-label="Jar of hemp dog treats"></div></div><div class="price">$ 385.00</div><div class="title">TW Treats1</div><div class="rate"><b>★★★★★</b> (77)</div></div>

<div class="abs card" style="left:393px;top:1063px"><div class="frame"><div class="shot tone-bottle" role="img" aria-label="Hemp oil dropper bottle"></div></div><div class="price">$ 385.00</div><div class="title">TW Extra Strength</div><div class="rate"><b>★★★★★</b> (77)</div></div>
<div class="abs card" style="left:615px;top:1063px"><div class="frame"><div class="shot tone-black" role="img" aria-label="Black dog collar"></div></div><div class="price">$ 385.00</div><div class="title">Black Roamer Collar</div><div class="rate"><b>★★★★★</b> (77)</div></div>
<div class="abs card" style="left:836px;top:1063px"><div class="frame"><div class="shot tone-wood" role="img" aria-label="Wooden memorial plaque"></div></div><div class="price">$ 385.00</div><div class="title">Pet Memorials</div><div class="rate"><b>★★★★★</b> (77)</div></div>

<div class="abs card" style="left:393px;top:1423px"><div class="frame"><div class="shot tone-hoodie" role="img" aria-label="Black hooded sweatshirt"></div></div><div class="price">$ 385.00</div><div class="title">Pet Lover Hoodie</div><div class="rate"><b>★★★★★</b> (77)</div></div>
<div class="abs card" style="left:615px;top:1423px"><div class="frame"><div class="shot tone-oil" role="img" aria-label="Hemp oil dropper bottle with box"></div></div><div class="price">$ 385.00</div><div class="title">Pet Memorials</div><div class="rate"><b>★★★★★</b> (77)</div></div>
<div class="abs card" style="left:836px;top:1423px"><div class="frame"><div class="shot tone-slate" role="img" aria-label="Slate grey dog collar"></div></div><div class="price">$ 385.00</div><div class="title">Slate Roamer Collar</div><div class="rate"><b>★★★★★</b> (77)</div></div>

<div class="abs divider"></div>
<div class="abs pager"><span class="on">1</span><span>2</span><span>3</span><span>4</span><span>›</span></div>

<!-- footer -->
<svg class="abs footer" viewBox="0 0 1200 368" preserveAspectRatio="none">
  <path d="M0 40 L30 14 L52 30 L70 6 L96 26 L120 10 L150 34 L175 8 L200 22 L232 4 L258 28 L290 10 L318 30 L350 6 L380 24 L410 12 L440 32 L470 6 L500 22 L530 10 L560 30 L590 8 L620 26 L650 12 L680 30 L710 4 L740 24 L770 10 L800 30 L830 6 L860 22 L890 12 L920 32 L950 8 L980 24 L1010 6 L1040 28 L1070 10 L1100 30 L1130 8 L1160 24 L1200 6 L1200 368 L0 368Z" fill="var(--footer)"/>
</svg>

<div class="abs" style="left:161px;top:1996px">
  <div class="f-head">Quick <span class="script">Links</span></div><div class="f-rule"></div>
  <ul class="f-links">
    <li>› Home</li><li>› About Us</li><li>› Pet Products ▾</li><li>› Our Mission</li><li>› Benefits</li><li>› Blog</li><li>› Contact Us</li>
  </ul>
</div>

<div class="abs" style="left:339px;top:1996px;width:250px">
  <div class="f-head">Contact <span class="script">Details</span></div><div class="f-rule"></div>
  <div style="position:relative;padding-left:29px;margin-top:18px">
    <svg class="ico" style="top:2px" viewBox="0 0 14 18"><path d="M7 0a6 6 0 0 1 6 6c0 5-6 12-6 12S1 11 1 6a6 6 0 0 1 6-6z" fill="#fff"/><circle cx="7" cy="6" r="2.3" fill="var(--footer)"/></svg>
    <div style="color:var(--teal);font-weight:700;font-size:14px">Tailwise</div>
    <div class="f-text" style="line-height:20px;margin-top:3px">Lorem ipsum dolor sit amet,<br>consectetur adipiscing elit</div>
  </div>
  <div style="position:relative;padding-left:29px;margin-top:12px;font-size:15px;color:#e6e6e6;letter-spacing:1px">
    <svg class="ico" style="top:1px" viewBox="0 0 16 16"><path d="M3 0l3 4-2 2c1 2 4 5 6 6l2-2 4 3-2 3C7 16 0 9 0 3z" fill="#fff"/></svg>(555) 014 2290</div>
  <div class="f-text" style="position:relative;padding-left:29px;margin-top:16px;font-size:13px">
    <svg class="ico" style="top:3px;height:12px" viewBox="0 0 16 12"><rect width="16" height="12" fill="#fff"/><path d="M0 0l8 6 8-6" fill="none" stroke="var(--footer)" stroke-width="1.5"/></svg>hello@tailwisepets.com</div>
</div>

<div class="abs" style="left:612px;top:1996px;width:240px">
  <div class="f-head">Newsletter <span class="script">Subscription</span></div><div class="f-rule"></div>
  <div class="f-text" style="margin-top:14px;line-height:17px;letter-spacing:1px;padding-left:2px">Subscribe to our newsletter<br>for latest updates.</div>
  <div class="field" style="margin-top:14px">Your Name*</div>
  <div class="field" style="margin-top:7px">Your Email Address*</div>
  <div class="signup" style="margin-top:8px">Sign Up</div>
</div>

<div class="abs" style="left:893px;top:1995px;width:150px">
  <div style="width:58px;height:58px;border-radius:50%;background:#d9d9d9;margin-left:42px"></div>
  <div style="font-size:22px;font-weight:700;color:#d9d9d9;margin-top:10px;text-align:center">Tailwise</div>
  <div class="f-head" style="margin-top:20px;padding-left:2px">Follow <span class="script">Us On:</span></div><div class="f-rule" style="margin-left:2px"></div>
  <div class="f-social" style="margin-top:20px;padding-left:3px"><span class="on"></span><span></span><span></span><span></span></div>
</div>

<div class="abs bottom">
  <span style="position:absolute;left:161px;top:21px">© 2019. Tailwise. All Right Reserved.</span>
  <span style="position:absolute;left:767px;top:23px">Privacy Policy &nbsp; / &nbsp; Terms &amp; Conditions</span>
</div>

</body>
</html>
```